2022 Grenache Hillside Vineyard Sketch Wine Label

Size:4"X4"
Wine: 2022 Grenache
Vineyard Name: Low Mill Vineyard
AVA: Solano County
Alcohol by Volume:15%
Volume:750ml
Must Feature a hillside vineyard on the label somehow, I picture it being a sketch but it doesn't have to be. Not looking for anything flashy or colorful but maybe a pop of color somewhere. I am not yet sure that I want to include our name, but you can try to work in "KMT" somewhere on the label if it fits the design.
The Label must include all the information listed above. The Grenache was grown in a hillside vineyard, so I wanted the label to prominently feature a hillside vineyard. You can layout the label however you see best, but the vintage and varietal should be prominent, the ABV can be in small type face but must be legible following FQD guidelines. If you are able to make the vineyard name pop as well that would be good.
You don't have to use these, but our standard fonts we use are:
For Varietal: Bianca
Secondary (vintage, AVA, Vineyard):Helvetica
ABV/Volume: PT Serif
Thank you, look forward to the results

```html
<!DOCTYPE html>
<html lang="en">
<head>
<meta charset="utf-8">
<title>2022 Grenache – Low Mill Vineyard Label</title>
<link rel="stylesheet" href="https://fonts.googleapis.com/css2?family=Alex+Brush&family=Oswald:wght@400;600&family=Roboto+Condensed:ital,wght@0,400;1,400&display=swap">
<style>
  :root {
    --label-black: #000000;
    --label-red: #ec1c24;
    --label-red-deep: #b3141a;
    --label-white: #ffffff;
    --page-bg: #e9e9e9;
  }
  html, body {
    margin: 0;
    padding: 0;
    width: 1200px;
    height: 1200px;
    overflow: hidden;
    background: var(--page-bg);
  }
  .label-canvas {
    display: block;
    width: 1200px;
    height: 1200px;
  }
  .label-base { fill: var(--label-black); }
  .frame-line { fill: none; stroke: var(--label-red); stroke-width: 4; }
  .title-band { fill: var(--label-red); }
  .band-rule { stroke: var(--label-black); stroke-width: 3; }
  .vintage-varietal {
    font-family: "Alex Brush", cursive;
    font-size: 118px;
    fill: var(--label-black);
  }
  .ava-tag { fill: var(--label-red); }
  .ava-text {
    font-family: "Oswald", sans-serif;
    font-size: 36px;
    font-weight: 400;
    fill: var(--label-black);
  }
  .scene-frame { fill: var(--label-black); stroke: var(--label-red); stroke-width: 4; }
  .abv-box { fill: var(--label-black); stroke: var(--label-red); stroke-width: 3; }
  .abv-text {
    font-family: "Roboto Condensed", sans-serif;
    font-style: italic;
    font-size: 36px;
    fill: var(--label-red);
  }
  .volume-box { fill: var(--label-red); }
  .volume-text {
    font-family: "Oswald", sans-serif;
    font-weight: 600;
    font-size: 62px;
    fill: var(--label-black);
  }
  .brand-seal { fill: var(--label-red); }
  .brand-ring { fill: none; stroke: var(--label-white); stroke-width: 3; }
  .brand-dot { fill: var(--label-white); }
  .brand-name {
    font-family: "Oswald", sans-serif;
    font-weight: 400;
    font-size: 52px;
    fill: var(--label-white);
    letter-spacing: 2px;
  }
</style>
</head>
<body>
<svg class="label-canvas" viewBox="706 9 1360 1360" xmlns="http://www.w3.org/2000/svg">
  <defs>
    <linearGradient id="hillside-tone" x1="0" y1="0" x2="0" y2="1">
      <stop offset="0" stop-color="#ec1c24"/>
      <stop offset="1" stop-color="#b3141a"/>
    </linearGradient>
  </defs>

  <!-- label body -->
  <rect class="label-base" x="854" y="275" width="1064" height="1063"/>

  <!-- outer and inner notched frames -->
  <path class="frame-line" d="M978 320 L1795 320 A80 80 0 0 0 1875 400 L1875 1217 A80 80 0 0 0 1795 1297 L978 1297 A80 80 0 0 0 898 1217 L898 400 A80 80 0 0 0 978 320 Z"/>
  <path class="frame-line" d="M990 343 L1783 343 A68 68 0 0 0 1852 411 L1852 1206 A68 68 0 0 0 1783 1274 L990 1274 A68 68 0 0 0 921 1206 L921 411 A68 68 0 0 0 990 343 Z"/>

  <!-- title band -->
  <polygon class="title-band" points="898,400 1875,458 1875,640 903,525"/>
  <line class="band-rule" x1="1630" y1="467" x2="1830" y2="492"/>
  <text class="vintage-varietal" x="1400" y="560" text-anchor="middle" transform="rotate(6.5 1400 530)">2022 Grenache</text>

  <!-- AVA tag -->
  <polygon class="ava-tag" points="975,560 1197,578 1192,618 970,600"/>
  <text class="ava-text" x="1086" y="603" text-anchor="middle" transform="rotate(4.6 1086 590)">Solano County</text>

  <!-- hillside vineyard scene -->
  <path class="scene-frame" d="M1105 665 L1700 665 A90 90 0 0 0 1790 755 L1790 1025 A90 90 0 0 0 1700 1115 L1105 1115 A90 90 0 0 0 1015 1025 L1015 755 A90 90 0 0 0 1105 665 Z"/>
  <path role="img" aria-label="Sketch of a hillside vineyard with rows of vines, trees and a winery barn on the ridge" fill="url(#hillside-tone)" d="M1115 688 L1690 688 A80 80 0 0 0 1770 768 L1770 1100 L1035 1100 L1035 768 A80 80 0 0 0 1115 688 Z"/>

  <!-- ABV -->
  <rect class="abv-box" x="1197" y="1055" width="425" height="38"/>
  <text class="abv-text" x="1410" y="1087" text-anchor="middle">15% Alcohol by Volume</text>

  <!-- volume -->
  <path class="volume-box" d="M1245 1140 L1528 1140 A17 17 0 0 0 1545 1157 L1545 1228 A17 17 0 0 0 1528 1245 L1245 1245 A17 17 0 0 0 1228 1228 L1228 1157 A17 17 0 0 0 1245 1140 Z"/>
  <text class="volume-text" x="1386" y="1216" text-anchor="middle">750ml</text>

  <!-- brand seal -->
  <circle class="brand-seal" cx="1400" cy="240" r="200"/>
  <circle class="brand-ring" cx="1400" cy="240" r="188"/>
  <circle class="brand-dot" cx="1400" cy="155" r="22"/>
  <text class="brand-name" x="1400" y="250" text-anchor="middle">Low Mill</text>
  <text class="brand-name" x="1400" y="315" text-anchor="middle">Vineyard</text>
</svg>
</body>
</html>
```